Dental Patient Education Single page-Multiple pages needed.

I am creating a unique dental patient education materials for resale. I work in the dental industry, training dentists and thier teams how to improve patient acceptance rates for treatment. I see a need that all patient education material is designed incorrectly. I want to fix this by creating patient education material that educated patients based on all of the treatment options for a diagnosed condition. Tradidional patient education material reads like a catalog of procedures. This format is not effective for helping the patient quickly understand the consequences of non treatment and the benefits and disadvantages of their treatment options. Specifics of the Job:The design images must be royalty free.I will provide the text.Initially there are for major diagnosed conditions: Infected Tooth Treatment Options, Single to Multiple Missing tooth Treatment Options, Full Arch of Missing Teeth Treatment Options, and Full Arch Fixed Dental Implant Treatment OptionsThe layout should mirror the attached sample of Single Missing Tooth Treatment Options.This is a project that will require edits and redesigned based on testing.I also need this in Adobe, so it can be customized/branded for a dental office.

Target Market(s)

Dental office professionals to educate patients.

Font styles to use
Sans Serif

Colors
3277b5

Requirements
Must have
• Professional look and feel
• Royalty free images
• Easy to read

```html
<!DOCTYPE html>
<html lang="en">
<head>
<meta charset="utf-8">
<title>Single Missing Tooth – Patient Education Flyer</title>
<link href="https://fonts.googleapis.com/css2?family=Montserrat:wght@400;500;600;800&display=swap" rel="stylesheet">
<style>
  :root{
    --blue:#3277b5;
    --blue-deep:#1f62a3;
    --navy:#163a66;
    --ink:#2c2f33;
    --paper:#ffffff;
    --panel:#e7e8ea;
    --stage:#3b3b3d;
    --photo-light:#dfeaf3;
    --photo-mid:#9cc3e2;
    --photo-skin:#ecd2bf;
    --gum:#e59a9e;
    --tooth:#f6f4ef;
  }
  *{box-sizing:border-box;margin:0;padding:0}
  html,body{width:1200px;height:776px;overflow:hidden;background:var(--stage)}
  body{font-family:"Montserrat",Arial,sans-serif;color:var(--ink)}
  .spread{position:relative;width:1200px;height:776px}
  .page{position:absolute;top:26px;width:560px;height:724px;background:var(--paper);overflow:hidden}
  .page--cover{left:24px}
  .page--inside{left:616px}

  /* cover */
  .cover-art{position:absolute;inset:0}
  .cover-title{position:absolute;left:40px;top:415px;color:var(--blue);font-weight:800;text-transform:uppercase;line-height:.98}
  .cover-title span{display:block}
  .cover-title .line-1{font-size:50px}
  .cover-title .line-2{font-size:47px;letter-spacing:.5px}
  .cover-band{position:absolute;left:30px;top:535px;width:510px;height:30px;background:var(--blue);transform:skewX(-14deg) rotate(-3deg);transform-origin:left center}
  .cover-band-text{position:absolute;left:44px;top:534px;color:#fff;font-size:14.5px;font-weight:500;transform:rotate(-3deg);transform-origin:left center;white-space:nowrap}
  .cover-body{position:absolute;left:40px;top:580px;width:380px;font-size:12px;font-weight:500;line-height:1.35;color:var(--ink)}
  .cover-body p+p{margin-top:10px}

  /* inside */
  .inside-panel{position:absolute;top:0;right:0;width:200px;height:100%;background:var(--panel)}
  .options{position:absolute;left:36px;top:42px;width:300px}
  .option+.option{margin-top:26px}
  .option h2{color:var(--blue);font-weight:800;font-size:15px;line-height:1.12;text-transform:uppercase;margin-bottom:8px}
  .option p{font-size:8.6px;line-height:1.42;text-align:justify}
  .visual{position:absolute;right:22px;width:160px;border-radius:2px}
  .visual--xray{top:40px;height:86px;background:radial-gradient(circle at 70% 60%,#c9ced4 0,#6d737a 30%,#2b2f34 75%)}
  .visual--implant{top:188px;height:100px;background:linear-gradient(180deg,var(--panel) 0,var(--gum) 40%,var(--tooth) 70%,var(--panel) 100%)}
  .visual--bridge{top:330px;height:112px;background:linear-gradient(180deg,var(--gum) 0,#f3c9c8 35%,var(--tooth) 65%,var(--panel) 100%)}
  .visual--denture{top:470px;height:130px;background:linear-gradient(180deg,var(--gum) 0,var(--tooth) 40%,#e8a2a5 75%,var(--panel) 100%)}
  .page-wave{position:absolute;left:0;bottom:0;width:560px;height:80px}
</style>
</head>
<body>
<main class="spread">

  <section class="page page--cover">
    <svg class="cover-art" width="560" height="724" viewBox="0 0 560 724">
      <defs>
        <linearGradient id="photoTone" x1="0" y1="0" x2="1" y2="1">
          <stop offset="0" stop-color="var(--photo-light)"/>
          <stop offset=".45" stop-color="var(--photo-skin)"/>
          <stop offset="1" stop-color="var(--photo-mid)"/>
        </linearGradient>
        <linearGradient id="paperFade" x1="0" y1="0" x2="0" y2="1">
          <stop offset="0" stop-color="#f1f2f4"/>
          <stop offset="1" stop-color="#ffffff"/>
        </linearGradient>
      </defs>
      <rect width="560" height="724" fill="url(#paperFade)"/>
      <path d="M0 30 C20 200 200 420 560 420 L560 395 C260 400 60 240 14 30 Z" fill="var(--blue)"/>
      <path d="M0 60 C40 240 230 430 560 440 L560 428 C240 420 40 250 0 40 Z" fill="var(--navy)" opacity=".35"/>
      <path role="img" aria-label="Photo of a smiling patient in the dental chair with gloved hands holding a mirror and probe"
            d="M22 0 L560 0 L560 392 C270 398 70 240 22 0 Z" fill="url(#photoTone)"/>
      <path d="M0 724 L0 712 C200 705 400 685 560 640 L560 724 Z" fill="var(--blue)"/>
      <path d="M0 724 L0 718 C200 712 400 698 560 668 L560 724 Z" fill="var(--navy)"/>
      <path d="M0 724 C200 720 400 710 560 690 L560 724 Z" fill="var(--blue-deep)"/>
    </svg>
    <h1 class="cover-title"><span class="line-1">Single</span><span class="line-2">Missing Tooth</span></h1>
    <div class="cover-band"></div>
    <div class="cover-band-text">A missing tooth is a serious issue. It can cause long-term</div>
    <div class="cover-body">
      <p>A missing tooth is a serious issue. It can cause long-term damage to facial structure, bone density and your ability to feel confident in your smile.</p>
      <p>Brightway Dental Studio has several options available to fix your missing tooth.</p>
    </div>
  </section>

  <section class="page page--inside">
    <div class="inside-panel"></div>
    <div class="options">
      <article class="option">
        <h2>Option 1:<br>Do Nothing</h2>
        <p>If you choose to do nothing at this time, the cost down the road can be substantial. $10,000+ for orthodontics to straighten out the teeth, implant, abutment and crown, bone grafting and possible sinus lift to replace lost bone.</p>
      </article>
      <article class="option">
        <h2>Option 2:<br>Dental Implant</h2>
        <p>The bad news is that a dental implant is the most expensive option. BUT the good news is it is the most effective, functional and aesthetically pleasing. A dental implant will keep the bone in that area of the jaw from atrophy. It helps maintain face shape and prevents "sunken face". The implant will prevent surrounding teeth from shifting and chances of losing the tooth decline. It will keep the teeth from shifting, and will prevent any future need to cut down the adjacent teeth. A dental implant is the nearest thing to a natural tooth available today.</p>
      </article>
      <article class="option">
        <h2>Option 3:<br>Dental Bridge</h2>
        <p>The good news here is that a bridge is less expensive than the implant option BUT you will continue to lose bone in that area over time. Food will get caught in the hard to reach areas and if not cleaned properly could mean you have to replace the bridge every 7 years. In addition, to secure the bridge, the adjacent teeth must be cut down in order to be used as anchors for the appliance. Why cut down two good teeth if we don't have to?</p>
      </article>
      <article class="option">
        <h2>Option 4:<br>The Removable Partial<br>Denture (RPD)</h2>
        <p>The good news here is that it's the least expensive option of the 3, but the BAD news is that your teeth have to come out every night. You won't be able to chew your food as well and your tongue will be uncomfortable with the big, bulky plastic sitting in your mouth all day.</p>
      </article>
    </div>
    <div class="visual visual--xray" role="img" aria-label="Dental X-ray showing the gap of a missing tooth"></div>
    <div class="visual visual--implant" role="img" aria-label="Illustration of a dental implant with abutment and crown"></div>
    <div class="visual visual--bridge" role="img" aria-label="Illustration of a dental bridge being placed over prepared teeth"></div>
    <div class="visual visual--denture" role="img" aria-label="Illustration of a removable partial denture fitting into the arch"></div>
    <svg class="page-wave" viewBox="0 0 560 80" aria-hidden="true">
      <path d="M0 80 L0 70 C200 50 400 30 560 0 L560 80 Z" fill="var(--blue)"/>
      <path d="M0 80 L0 76 C200 62 400 48 560 30 L560 80 Z" fill="var(--navy)"/>
      <path d="M0 80 C220 74 420 66 560 56 L560 80 Z" fill="var(--blue-deep)"/>
    </svg>
  </section>

</main>
</body>
</html>
```